Sports field reservations application

We are developing a website for the reservation of sports grounds (Tennis, squash, Paddle).

We need ;
A login page for the administrator
A look for the administration page, dashboard
A look for the pages (list of members, list of courses)
A look for the member file
A look for the payment module

A login page for the member
a look to see the land available
An "agenda" look to see the courts available by type (Tennis, Squash, Paddle, ect ...)
A look to make the reservation form.

We develop in webdev (html).

We develop a website for the reservation of sports field (Tennis, squash, Paddle).

We need;
A look for the member card

a look to see the available lands
A look "agenda" to see the available land by type (Tennis, Squash, Paddle, ect ...)
A look to make the booking form.

Male - 30-45 years
Athletic

Coded - Design and coding required

5+ page

Serif

Designer to choose colors to be used in the design.

• Responsive Mobile - tablet - pc - mac

```html
<!DOCTYPE html>
<html lang="en">
<head>
<meta charset="utf-8">
<title>CourtLine – Court Booking</title>
<link rel="stylesheet" href="https://fonts.googleapis.com/css2?family=Open+Sans:wght@400;600;700&family=Montserrat:wght@600;700&display=swap">
<style>
  :root{
    --orange:#f39200;
    --orange-soft:#fde3c4;
    --green:#36d43a;
    --green-dark:#1f8a2a;
    --ink:#3a3a3a;
    --ink-soft:#8a8a8a;
    --line:#e3e3e3;
    --panel:#ffffff;
    --app-bg:#f2f2f2;
    --page:#ffffff;
    --curve:#fcefe6;
    --dark-slot:#2d2d2d;
  }
  *{box-sizing:border-box;margin:0;padding:0}
  html,body{width:748px;height:1200px;overflow:hidden;background:var(--page);font-family:"Open Sans",Arial,sans-serif;color:var(--ink)}
  .board{position:relative;width:748px;height:1200px;overflow:hidden}
  .board-curve{position:absolute;inset:0}

  .brand{position:absolute;top:52px;left:0;width:748px;display:flex;justify-content:center;align-items:center;gap:14px}
  .brand-mark{width:54px;height:54px;border-radius:50%;background:var(--ink)}
  .brand-name{font-family:"Montserrat",Arial,sans-serif;font-weight:700;font-size:38px;color:var(--ink);line-height:1}
  .brand-tag{font-family:"Montserrat",Arial,sans-serif;font-weight:700;font-size:38px;color:var(--ink);display:none}
  .brand-text small{display:block;font-family:"Montserrat",Arial,sans-serif;font-weight:600;font-size:15px;color:var(--ink);margin-top:4px;letter-spacing:.5px}

  /* screen frame, designed at 1000 x 480 then scaled */
  .screen-slot{position:absolute;overflow:hidden;box-shadow:0 2px 10px rgba(0,0,0,.12)}
  .screen{width:1000px;height:480px;transform-origin:0 0;background:var(--app-bg);position:relative;display:flex;flex-direction:column}
  .topbar{height:44px;background:var(--panel);border-bottom:1px solid var(--line);display:flex;justify-content:flex-end;align-items:center;gap:14px;padding-right:22px}
  .search{width:150px;height:22px;border:1px solid var(--line);border-radius:2px;font-size:11px;color:var(--ink-soft);padding:3px 8px}
  .avatar{width:26px;height:26px;border-radius:50%;background:#c9c9c9}
  .body{flex:1;display:flex;min-height:0}
  .sidebar{width:180px;background:var(--panel);border-right:1px solid var(--line);display:flex;flex-direction:column;padding:14px 0}
  .side-brand{display:flex;align-items:center;gap:8px;padding:0 16px 16px;margin-top:-52px}
  .side-brand i{width:26px;height:26px;border-radius:50%;background:var(--ink)}
  .side-brand b{font-family:"Montserrat",Arial,sans-serif;font-size:18px;font-weight:700;color:var(--ink)}
  .menu{list-style:none;margin-top:24px}
  .menu li{font-size:13px;padding:12px 18px;border-bottom:1px solid var(--line);display:flex;gap:8px;align-items:center}
  .menu li::before{content:"";width:9px;height:9px;border-radius:50%;background:var(--orange)}
  .logout{margin:auto 18px 6px;background:var(--orange);color:#fff;font-size:12px;font-weight:600;text-align:center;padding:6px 0;width:90px}
  .main{flex:1;padding:18px 26px;min-width:0}
  .footer{height:28px;background:var(--orange);color:#fff;font-size:11px;display:flex;align-items:center;justify-content:center}

  .activity-title{text-align:center;color:var(--orange);font-family:"Montserrat",Arial,sans-serif;font-weight:700;font-size:22px;margin:8px 0 18px}
  .activities{display:grid;grid-template-columns:repeat(3,1fr);row-gap:16px;width:560px;margin:0 auto}
  .activity{display:flex;flex-direction:column;align-items:center;gap:8px}
  .activity-photo{width:120px;height:120px;border-radius:50%}
  .activity-name{font-size:12px;font-weight:700;text-transform:uppercase}
  .clay{background:radial-gradient(circle at 40% 40%,#c9d84a,#7a6a2a)}
  .resin{background:radial-gradient(circle,#3a3a3a,#1a1a1a)}
  .carpet{background:radial-gradient(circle,#3fa53c,#1e6b24)}
  .indoor{background:radial-gradient(circle,#d07a3c,#8a3e1c)}
  .squash{background:radial-gradient(circle,#e9e4da,#9fb6cc)}
  .padel{background:radial-gradient(circle,#3d8fd1,#1b4f86)}

  /* agenda */
  .mini-cal{margin:-6px 16px 0;font-size:9px;color:var(--ink-soft);display:grid;grid-template-columns:repeat(7,1fr);gap:3px;text-align:center}
  .mini-cal b{grid-column:1/-1;color:var(--orange);font-size:11px;margin-bottom:2px}
  .agenda-head{background:var(--orange);color:#fff;font-size:13px;font-weight:600;padding:7px 12px;width:180px}
  .agenda-date{display:flex;justify-content:space-between;align-items:center;margin:14px 0 8px}
  .agenda-date strong{color:var(--orange);font-size:17px}
  .agenda-date span{font-size:11px;border:1px solid var(--line);background:#fff;padding:3px 10px}
  .grid{background:#fff;border:1px solid var(--line);font-size:10px}
  .grid-row{display:grid;grid-template-columns:110px repeat(6,1fr);border-bottom:1px solid var(--line);height:22px;align-items:center;position:relative}
  .grid-row > span{padding-left:6px}
  .slot{position:absolute;top:3px;height:16px}
  .slot.free{background:var(--green)}
  .slot.taken{background:var(--dark-slot)}
  .slot.mix{background:var(--green-dark)}
</style>
</head>
<body>
<div class="board">
  <svg class="board-curve" width="748" height="1200" viewBox="0 0 748 1200" aria-hidden="true">
    <path d="M560 0 C 720 200, 760 420, 748 620 L 748 0 Z" fill="var(--curve)"/>
    <path d="M748 700 C 640 820, 620 1000, 748 1200 Z" fill="var(--curve)"/>
  </svg>

  <header class="brand">
    <span class="brand-mark"></span>
    <div class="brand-text">
      <div class="brand-name">CourtLine</div>
      <small>Réservez votre terrain</small>
    </div>
  </header>

  <!-- agenda screen, small -->
  <div class="screen-slot" style="left:40px;top:330px;width:190px;height:91px">
    <div class="screen" style="transform:scale(.19)">
      <div class="topbar"><div class="search">Search</div><div class="avatar"></div></div>
      <div class="body">
        <aside class="sidebar">
          <div class="side-brand"><i></i><b>CourtLine</b></div>
          <ul class="menu"><li>My Next Bookings</li><li>My Invitations</li><li>My Account</li></ul>
          <div class="logout">Log out</div>
        </aside>
        <section class="main">
          <div class="agenda-head">Calendar Courts</div>
          <div class="agenda-date"><strong>‹ Tuesday December 11 ›</strong><span>All Courts</span></div>
          <div class="grid">
            <div class="grid-row"><span>Time</span><span>08:00</span><span>10:00</span><span>12:00</span><span>14:00</span><span>16:00</span><span>18:00</span></div>
            <div class="grid-row"><span>Mixed</span><i class="slot free" style="left:110px;right:0"></i></div>
            <div class="grid-row"><span>Court 1</span><i class="slot mix" style="left:110px;right:0"></i></div>
            <div class="grid-row"><span>Court 2</span><i class="slot taken" style="left:110px;right:0"></i></div>
          </div>
        </section>
      </div>
      <div class="footer">Legal Notice | Booking solution by CourtLine</div>
    </div>
  </div>

  <!-- activity screen, large -->
  <div class="screen-slot" style="left:250px;top:170px;width:460px;height:221px">
    <div class="screen" style="transform:scale(.46)">
      <div class="topbar"><div class="search">Search</div><div class="avatar"></div></div>
      <div class="body">
        <aside class="sidebar">
          <div class="side-brand"><i></i><b>CourtLine</b></div>
          <ul class="menu"><li>My Next Bookings</li><li>My Invitations</li><li>My Account</li></ul>
          <div class="logout">Log out</div>
        </aside>
        <section class="main">
          <h2 class="activity-title">CHOOSE YOUR ACTIVITY</h2>
          <div class="activities">
            <div class="activity"><div class="activity-photo clay" role="img" aria-label="Outdoor clay tennis court"></div><span class="activity-name">Outdoor clay courts</span></div>
            <div class="activity"><div class="activity-photo resin" role="img" aria-label="Exterior resin court"></div><span class="activity-name">Exterior resin</span></div>
            <div class="activity"><div class="activity-photo carpet" role="img" aria-label="Interior carpet court"></div><span class="activity-name">Interior carpets</span></div>
          </div>
        </section>
      </div>
      <div class="footer">Legal Notice | Booking solution by CourtLine</div>
    </div>
  </div>

  <!-- activity screen -->
  <div class="screen-slot" style="left:150px;top:585px;width:530px;height:254px">
    <div class="screen" style="transform:scale(.53)">
      <div class="topbar"><div class="search">Search</div><div class="avatar"></div></div>
      <div class="body">
        <aside class="sidebar">
          <div class="side-brand"><i></i><b>CourtLine</b></div>
          <ul class="menu"><li>My Next Bookings</li><li>My Invitations</li><li>My Account</li><li>My Personal Info</li></ul>
          <div class="logout">Log out</div>
        </aside>
        <section class="main">
          <h2 class="activity-title">CHOOSE YOUR ACTIVITY</h2>
          <div class="activities">
            <div class="activity"><div class="activity-photo clay" role="img" aria-label="Outdoor clay tennis court"></div><span class="activity-name">Outdoor clay courts</span></div>
            <div class="activity"><div class="activity-photo resin" role="img" aria-label="Exterior resin court"></div><span class="activity-name">Exterior resin</span></div>
            <div class="activity"><div class="activity-photo carpet" role="img" aria-label="Interior carpet court"></div><span class="activity-name">Interior carpets</span></div>
            <div class="activity"><div class="activity-photo indoor" role="img" aria-label="Indoor clay court"></div><span class="activity-name">Indoor clay courts</span></div>
            <div class="activity"><div class="activity-photo squash" role="img" aria-label="Squash court"></div><span class="activity-name">Squash</span></div>
            <div class="activity"><div class="activity-photo padel" role="img" aria-label="Padel court"></div><span class="activity-name">Padel</span></div>
          </div>
        </section>
      </div>
      <div class="footer">Legal Notice | Association — a booking solution by CourtLine</div>
    </div>
  </div>

  <!-- agenda screen -->
  <div class="screen-slot" style="left:150px;top:870px;width:530px;height:254px">
    <div class="screen" style="transform:scale(.53)">
      <div class="topbar"><div class="search">Search</div><div class="avatar"></div></div>
      <div class="body">
        <aside class="sidebar">
          <div class="side-brand"><i></i><b>CourtLine</b></div>
          <div class="mini-cal"><b>December</b><span>M</span><span>T</span><span>W</span><span>T</span><span>F</span><span>S</span><span>S</span><span>10</span><span>11</span><span>12</span><span>13</span><span>14</span><span>15</span><span>16</span></div>
          <ul class="menu"><li>My Next Bookings</li><li>My Invitations</li><li>My Account</li><li>My Personal Info</li></ul>
          <div class="logout">Log out</div>
        </aside>
        <section class="main">
          <div class="agenda-head">Calendar Courts ▾</div>
          <div class="agenda-date"><strong>‹ Tuesday December 11 ›</strong><span>All Courts ▾</span></div>
          <div class="grid">
            <div class="grid-row"><span>Today</span><span>Tue 11/12</span><span>Wed 12/12</span><span>Thu 13/12</span><span>Fri 14/12</span><span>Sat 15/12</span><span>Sun 16/12</span></div>
            <div class="grid-row"><span>08:00</span><span>09:00</span><span>10:00</span><span>11:00</span><span>12:00</span><span>13:00</span><span>14:00</span></div>
            <div class="grid-row"><span>Mixed Tennis</span><i class="slot free" style="left:110px;right:0"></i></div>
            <div class="grid-row"><span>Court 1 - Clay</span><i class="slot free" style="left:110px;right:0"></i></div>
            <div class="grid-row"><span>Court 2 - Resin</span><i class="slot mix" style="left:110px;right:120px"></i><i class="slot free" style="right:0;width:120px"></i></div>
            <div class="grid-row"><span>Court 3 - Carpet</span><i class="slot taken" style="left:110px;right:0"></i></div>
            <div class="grid-row"><span>Court 4 - Indoor</span><i class="slot taken" style="left:110px;right:240px"></i><i class="slot mix" style="right:0;width:240px"></i></div>
          </div>
        </section>
      </div>
      <div class="footer">Legal Notice | Association — a booking solution by CourtLine</div>
    </div>
  </div>
</div>
</body>
</html>
```